" Trata-se de consultório médico particular, de especialidade em gastroenterologia, cujos impressos serao utilizados como cartao de visita, receituários e envelopes. "

```html
<!DOCTYPE html>
<html lang="pt-BR">
<head>
<meta charset="utf-8">
<title>Helena Vasconi Duarte – Gastroenterologia · Papelaria</title>
<link href="https://fonts.googleapis.com/css2?family=Cormorant+SC:wght@500&family=Montserrat:wght@300;400&display=swap" rel="stylesheet">
<style>
  :root {
    --backdrop: #e9e7ee;
    --paper: #ffffff;
    --paper-tint: #f1f0f8;
    --lilac: #9d9ad8;
    --lilac-deep: #8c89c4;
    --ink: #8481b6;
    --ink-soft: #a3a1c8;
    --shadow: rgba(60, 50, 90, 0.18);
  }
  * { margin: 0; padding: 0; box-sizing: border-box; }
  html, body { width: 1200px; height: 1200px; overflow: hidden; }
  body {
    background: var(--backdrop);
    position: relative;
    font-family: "Montserrat", sans-serif;
    color: var(--ink);
  }

  /* Envelope */
  .envelope {
    position: absolute;
    left: 266px; top: 199px;
    width: 672px; height: 384px;
    background: linear-gradient(180deg, var(--paper) 0%, var(--paper-tint) 100%);
    box-shadow: 0 6px 18px var(--shadow);
    overflow: hidden;
  }
  .envelope__flap { position: absolute; left: 0; top: 0; width: 672px; height: 48px; }
  .envelope__accent {
    position: absolute; left: 70px; top: 70px;
    width: 300px; height: 300px; border-radius: 50%;
    background: var(--lilac); opacity: 0.12;
  }
  .envelope__brand {
    position: absolute; left: 470px; top: 226px; width: 190px;
    text-align: center;
  }
  .envelope__brand .brand-mark { width: 14px; height: 14px; margin: 0 auto 4px; }
  .envelope__brand .brand-name { font-size: 13px; }
  .envelope__brand .brand-field { font-size: 6px; letter-spacing: 1px; margin-top: 2px; }
  .envelope__contact {
    position: absolute; left: 506px; top: 310px;
    font-size: 8px; line-height: 12.5px; color: var(--ink);
    list-style: none;
  }

  /* Business card */
  .card {
    position: absolute;
    left: 269px; top: 648px;
    width: 662px; height: 372px;
    background: var(--paper);
    box-shadow: 0 6px 18px var(--shadow);
  }
  .card__brand {
    position: absolute; left: 16px; top: 128px; width: 282px;
    text-align: center;
  }
  .card__brand .brand-mark { width: 26px; height: 26px; margin: 0 auto 14px; }
  .card__brand .brand-name { font-size: 24px; }
  .card__brand .brand-field { font-size: 10px; letter-spacing: 2.4px; margin-top: 2px; }

  /* Shared brand type */
  .brand-mark { border-radius: 50%; background: var(--lilac); }
  .brand-name {
    font-family: "Cormorant SC", serif; font-weight: 500;
    color: var(--ink); letter-spacing: 0.5px; white-space: nowrap;
  }
  .brand-field {
    font-family: "Montserrat", sans-serif; font-weight: 300;
    color: var(--ink-soft); white-space: nowrap;
  }
</style>
</head>
<body>
  <section class="envelope" aria-label="Envelope">
    <svg class="envelope__flap" viewBox="0 0 672 48" aria-hidden="true">
      <polygon points="0,0 672,0 672,34 640,48 32,48 0,34" fill="var(--lilac)"/>
      <polygon points="0,34 32,48 640,48 672,34 672,36 640,50 32,50 0,36" fill="var(--lilac-deep)" opacity="0.5"/>
    </svg>
    <div class="envelope__accent" aria-hidden="true"></div>
    <div class="envelope__brand">
      <div class="brand-mark" aria-hidden="true"></div>
      <div class="brand-name">Helena Vasconi Duarte</div>
      <div class="brand-field">Gastroenterologia Clínica</div>
    </div>
    <ul class="envelope__contact">
      <li>(21) 4410 2786</li>
      <li>Rua das Acácias, 418</li>
      <li>Ed. Monte Claro, sala 205</li>
      <li>Jardim Alto, Serra Nova RJ</li>
      <li>CEP 24710-330</li>
    </ul>
  </section>

  <section class="card" aria-label="Cartão de visita">
    <div class="card__brand">
      <div class="brand-mark" aria-hidden="true"></div>
      <div class="brand-name">Helena Vasconi Duarte</div>
      <div class="brand-field">Gastroenterologia</div>
    </div>
  </section>
</body>
</html>
```